Poster Design For Obstacle Run

Design a poster for the Crow Ridge Obstacle run.
Text: Crow Ridge Obstacle Run. May 12th, 2018. Sittard. www.crowridgedash.nl. I have added a lot of pictures.
Furthermore, the logo should be included. As an example I included a poster from the ironbark race that we really like (ironbark team challenge) and also. Feel free to take a look at our website for inspiration: www.crowridgedash.nl

```html
<!DOCTYPE html>
<html lang="en">
<head>
<meta charset="utf-8">
<title>Crow Ridge Obstacle Run — Poster</title>
<link rel="stylesheet" href="https://fonts.googleapis.com/css2?family=Bebas+Neue&family=Oswald:wght@300&display=swap">
<style>
  :root {
    --orange: #e2532a;
    --orange-deep: #c23c1c;
    --black: #0d0d0d;
    --ink: #161616;
    --white: #ffffff;
    --grey: #8a8a8a;
    --photo-mono-1: #2b2b2b;
    --photo-mono-2: #8f8f8f;
  }
  html, body { margin: 0; padding: 0; overflow: hidden; background: var(--black); }
  .poster {
    position: relative;
    width: 849px;
    height: 1200px;
    overflow: hidden;
    background: radial-gradient(circle at 50% 82%, #262626 0%, #171717 45%, #0f0f0f 100%);
    font-family: "Oswald", "Arial Narrow", sans-serif;
  }
  .block { position: absolute; }
  .photo-tires { left: 0; top: 0; width: 312px; height: 386px;
    background: linear-gradient(160deg, #1a1a1a 0%, #4a4a4a 55%, #bdbdbd 80%, #2a2a2a 100%); }
  .photo-hands { left: 312px; top: 0; width: 194px; height: 194px;
    background: linear-gradient(135deg, var(--orange-deep) 0%, #e06a3e 55%, #f3a27a 100%); }
  .photo-net { left: 506px; top: 0; width: 296px; height: 386px;
    background: radial-gradient(ellipse at 45% 55%, #f08a5e 0%, var(--orange) 45%, #7a2410 100%); }
  .photo-rope { left: 0; top: 386px; width: 506px; height: 332px;
    background: linear-gradient(120deg, #d6d6d6 0%, var(--photo-mono-2) 35%, var(--photo-mono-1) 70%, #111 100%); }
  .edge-strip { left: 802px; top: 0; width: 47px; height: 386px; background: var(--ink); }
  .edge-accent { left: 802px; top: 370px; width: 47px; height: 16px; background: var(--orange); }
  .base-accent { left: 0; top: 718px; width: 254px; height: 16px; background: var(--orange); }
  .title-panel { left: 506px; top: 386px; width: 343px; height: 332px; background: var(--black); }

  .ready {
    position: absolute; left: 250px; top: 200px; width: 62px; height: 186px;
    writing-mode: vertical-rl; transform: rotate(180deg);
    color: var(--orange); font-weight: 300; font-size: 76px; line-height: 62px;
    letter-spacing: -1px; text-align: left; margin: 0;
  }
  .date-box {
    left: 312px; top: 194px; width: 194px; height: 192px; background: var(--orange);
    display: flex; flex-direction: column; align-items: center; justify-content: center;
    font-weight: 300; line-height: 0.92; text-align: center;
  }
  .date-box .day { color: var(--white); font-size: 60px; }
  .date-box .year { color: var(--black); font-size: 86px; letter-spacing: -2px; }
  .date-box .city { color: var(--white); font-size: 50px; }

  .title {
    position: absolute; left: 534px; top: 405px; width: 270px; margin: 0;
    font-family: "Bebas Neue", "Oswald", sans-serif; font-weight: 400;
    color: var(--orange); line-height: 0.82; text-align: center;
  }
  .title span { display: block; }
  .title .line-name { font-size: 86px; letter-spacing: 0px; }
  .title .line-obstacle { font-size: 92px; letter-spacing: 0px; margin-top: 4px; }
  .title .line-run { font-size: 236px; letter-spacing: 2px; line-height: 0.78; margin-top: 6px; }

  .brand-mark {
    position: absolute; left: 0; width: 849px; top: 960px;
    display: flex; align-items: center; justify-content: center; gap: 10px;
    color: var(--orange); font-weight: 300; font-size: 28px; letter-spacing: 1px;
  }
  .brand-mark .dot { width: 16px; height: 16px; border-radius: 50%; background: var(--orange); }
  .website {
    position: absolute; left: 0; width: 849px; top: 1126px; text-align: center;
    color: var(--grey); font-weight: 300; font-size: 22px; letter-spacing: 5px;
  }
</style>
</head>
<body>
  <main class="poster">
    <div class="block photo-tires" role="img" aria-label="Black and white photo of runners stepping through a tyre obstacle"></div>
    <div class="block photo-hands" role="img" aria-label="Orange-toned photo of a muddy hand gripping an obstacle"></div>
    <div class="block photo-net" role="img" aria-label="Orange-toned photo of a runner crawling through mud under a rope net"></div>
    <div class="block photo-rope" role="img" aria-label="Black and white photo of a muddy arm pulling a rope up a wall"></div>
    <div class="block edge-strip"></div>
    <div class="block edge-accent"></div>
    <div class="block title-panel"></div>
    <div class="block base-accent"></div>

    <p class="ready">READY?</p>

    <div class="block date-box">
      <span class="day">MAY 12</span>
      <span class="year">2018</span>
      <span class="city">SITTARD</span>
    </div>

    <h1 class="title">
      <span class="line-name">CROW RIDGE</span>
      <span class="line-obstacle">OBSTACLE</span>
      <span class="line-run">RUN</span>
    </h1>

    <div class="brand-mark">
      <span class="dot"></span>
      <span class="brand-name">Crow Ridge Obstacle Run</span>
    </div>

    <div class="website">WWW.CROWRIDGEDASH.NL</div>
  </main>
</body>
</html>
```